Verdane Clinical Spa needs an eye-catching poster to help promote our largest sale of spring!

We need a poster that will go on the back of the doors in the patient rooms. Our medical spa is professional and high-end, so we want the poster to look sophisticated, yet very eye-catching.
This project is for our Marigold Jubilee special, our second largest sale of the year.

Name: Marigold Jubilee
Slogan: Let Your Beauty Bloom
Sale: The More You Buy, The More You Save

Choose from your favorite spa services
NEVRIL, Laser Treatments, Microderms, and More!

It would be great to have something blooming. Flowers, or somehow make a woman look like she's blooming.

I am attaching a visual description of our special. However, the poster should NOT include the pricing tiers. I am also attaching our business logo. Thank you!!

Target Market(s)

A majority are women, but some are men. Around 25-55 in age. Middle to upper class who are likely to spend more money.

Industry/Entity Type

Medical

Font styles to use
Sans Serif
Script

Colors

Designer to choose colors to be used in the design.

Requirements
Must have
• Name of promotion: Marigold Jubilee
• Slogan: "Let Your Beauty Bloom"
• Concept "The more you buy, the more you save on your favorite spa services"
• Select from your favorite spa services such as NEVRIL, laser treatments, microderms, and more!
• Website: VerdaneSpaDeals.com
• Our logo (attached)
Nice to have
• Modern and creative design. Somehow tying in the "Let your beauty bloom" theme. We don't want the focus to be "The more you buy the more you save"
• We are looking for a unique design that is unlike traditional medical spas in the area that typically include a lot of white and a lot of overly photoshopped images.
• Creativity is key! Something that's different than just text and images. We would be so excited to see that!
Should not have
• Not too much text, but enough to get the point across.

```html
<!DOCTYPE html>
<html lang="en">
<head>
<meta charset="utf-8">
<title>Marigold Jubilee – Verdane Clinical Spa</title>
<link rel="stylesheet" href="https://fonts.googleapis.com/css2?family=Lato:wght@300;400;700;900&family=Cormorant+Garamond:ital,wght@1,500&display=swap">
<style>
  :root {
    --navy: #2a2466;
    --magenta: #d6185a;
    --blush: #f3cfe2;
    --blush-deep: #e3a9c9;
    --lilac: #d9b8dc;
    --white: #ffffff;
    --leaf: #b9dca6;
    --ink: #2b2b2b;
  }
  * { margin: 0; padding: 0; box-sizing: border-box; }
  html, body { width: 848px; height: 1200px; overflow: hidden; background: var(--white); }
  .poster {
    position: relative; width: 848px; height: 1200px; overflow: hidden;
    font-family: "Lato", sans-serif; color: var(--navy);
  }
  .blossom-scene {
    position: absolute; inset: 0;
    background:
      radial-gradient(ellipse 300px 380px at 650px 560px, #ecc3d5 0%, rgba(236,195,213,0) 70%),
      radial-gradient(ellipse 260px 300px at 720px 980px, #c9b3d8 0%, rgba(201,179,216,0) 70%),
      linear-gradient(160deg, #f6dbe9 0%, var(--blush) 45%, var(--blush-deep) 100%);
  }
  .brand-corner { position: absolute; top: 0; left: 0; width: 848px; height: 300px; }
  .brand {
    position: absolute; top: 70px; left: 406px; display: flex; align-items: center; gap: 14px;
  }
  .brand-dot { width: 46px; height: 46px; border-radius: 50%; background: var(--leaf); }
  .brand-name { font-family: "Lato", sans-serif; font-weight: 400; font-size: 38px; color: var(--ink); white-space: nowrap; }
  .promo-title {
    position: absolute; top: 228px; left: 30px;
    font-family: "Lato", sans-serif; font-weight: 300; font-size: 112px; line-height: 0.98;
    color: var(--white); letter-spacing: 1px;
    -webkit-text-stroke: 1.5px var(--navy);
    text-shadow: 0 0 6px var(--navy), 0 0 14px rgba(42,36,102,0.7);
  }
  .slogan {
    position: absolute; top: 510px; left: 30px;
    font-family: "Cormorant Garamond", serif; font-style: italic; font-weight: 500;
    font-size: 42px; color: var(--navy); letter-spacing: 1px;
  }
  .dates {
    position: absolute; top: 606px; left: 112px; transform: rotate(-5deg);
    font-weight: 900; font-size: 34px; line-height: 1; color: var(--magenta); text-align: center;
  }
  .services-intro { position: absolute; top: 740px; left: 20px; font-size: 28px; line-height: 0.95; color: var(--navy); }
  .services-list { position: absolute; top: 826px; left: 20px; font-size: 35px; line-height: 1.05; color: var(--navy); }
  .savings-badge { position: absolute; top: 665px; left: 440px; width: 240px; height: 240px; }
  .savings-text {
    position: absolute; top: 714px; left: 470px; width: 180px; transform: rotate(-14deg);
    font-size: 27px; line-height: 1; color: var(--navy); text-align: center;
  }
  .savings-text b { color: var(--magenta); font-weight: 900; font-size: 32px; }
  .product-ribbon { position: absolute; top: 948px; left: 300px; width: 548px; height: 120px; }
  .ribbon-band { position: absolute; top: 30px; left: 10px; width: 520px; height: 70px; background: var(--navy); transform: rotate(-5deg) skewX(-14deg); }
  .ribbon-label {
    position: absolute; top: 14px; left: 70px; width: 300px; height: 84px; background: var(--magenta);
    transform: rotate(-5deg); color: var(--white); font-weight: 900; font-size: 38px;
    display: flex; align-items: center; justify-content: center;
  }
  .ribbon-offer {
    position: absolute; top: 28px; left: 375px; transform: rotate(-5deg);
    color: var(--white); font-weight: 700; font-size: 42px;
  }
  .ribbon-offer small { font-size: 26px; font-weight: 400; }
  .site-bar {
    position: absolute; left: 0; bottom: 0; width: 848px; height: 58px; background: var(--navy);
    display: flex; align-items: center; justify-content: center;
    color: var(--white); font-weight: 700; font-size: 28px; letter-spacing: 4px;
  }
</style>
</head>
<body>
<main class="poster">
  <div class="blossom-scene" role="img" aria-label="Soft pink cherry blossom branches framing a woman in a plaid shirt"></div>

  <svg class="brand-corner" viewBox="0 0 848 300" aria-hidden="true">
    <path d="M397 0 C400 120 370 190 286 217 C470 190 700 215 848 277 L848 0 Z" fill="#ffffff"/>
    <path d="M397 0 C400 120 370 190 286 217 C470 190 700 215 848 277" fill="none" stroke="#d6185a" stroke-width="5"/>
  </svg>

  <div class="brand">
    <span class="brand-dot"></span>
    <span class="brand-name">Verdane Clinical Spa</span>
  </div>

  <h1 class="promo-title">MARIGOLD<br>JUBILEE</h1>
  <p class="slogan">let your beauty bloom</p>

  <p class="dates">APRIL 20<br>JUNE 2</p>

  <p class="services-intro">Choose from your favorite<br>spa services</p>
  <p class="services-list">NEVRIL,<br>Laser Treatments<br>Microderms, and More!</p>

  <svg class="savings-badge" viewBox="0 0 240 240" aria-hidden="true">
    <defs>
      <radialGradient id="badgeGlow">
        <stop offset="0.72" stop-color="#d6185a"/>
        <stop offset="1" stop-color="#d6185a" stop-opacity="0"/>
      </radialGradient>
    </defs>
    <circle cx="120" cy="120" r="120" fill="url(#badgeGlow)"/>
    <polygon fill="#ffffff" points="120,28 128,40 139,30 144,43 157,36 158,50 172,46 170,60 184,59 179,72 193,74 186,86 199,91 189,101 200,109 189,117 199,126 187,132 195,143 182,147 187,160 173,161 175,175 161,173 160,187 147,182 144,196 132,188 126,201 116,191 108,202 102,190 92,199 88,186 76,192 75,178 62,182 64,168 50,169 55,156 42,153 50,142 38,136 48,127 38,118 49,111 40,101 52,96 46,84 59,82 56,69 69,70 68,56 81,60 83,46 95,52 99,39 110,47 " transform="rotate(8 120 120)"/>
  </svg>
  <p class="savings-text">The More<br>You <b>Buy</b><br>The More<br>You <b>Save</b></p>

  <div class="product-ribbon">
    <div class="ribbon-band"></div>
    <div class="ribbon-label">Just products</div>
    <div class="ribbon-offer">10%<small>off</small></div>
  </div>

  <footer class="site-bar">VerdaneSpaDeals.com</footer>
</main>
</body>
</html>
```